My Book needs a front and back cover design

I need you to design my front and back cover of my book. The title of my book is : Lanterns Past Harbour
Tide Notes
7 paths to gardening calmly always

The picture that I uploaded needs to be on the front cover. On the back cover it should be excerpt from Chapter One like this :

As years have gone by I have become much more conscious about my problem with stuttering, more able to relax my muscles to alleviate it. At the age of 20, I realized that stuttering is like a demon in my head that needs to be killed and that nothing is wrong with me. Furthermore, no one can help me but myself. I'm holding the key of my future. Everything is just in my head.

With this book, I want to help you realize that nobody can help you fix your stuttering better than yourself. There's no quick-get-rid-of-stuttering cure. The cure lies inside of you.

- Lorcan Vittel, excerpt from Chapter One
----------------------------------------------------------------------------------

My name also needs to be located on the front cover.

Target Market(s)

80 million people who stutter each day

Industry/Entity Type

Psychology

Font styles to use
Serif
Sans Serif

Colors
1b1b1b
000000
333333

Requirements
Must have
• Front Cover : Full Title and subtitle and my name and my picture
• Back Cover : Excerpt from my Chapter One with my name below just as I have described in my project description
Nice to have
• Maybe black background would be the best for the front cover.

```html
<!DOCTYPE html>
<html lang="en">
<head>
<meta charset="utf-8">
<title>Lanterns Past Harbour – Book Cover</title>
<link href="https://fonts.googleapis.com/css2?family=Arimo:wght@700&family=Tinos:wght@700&display=swap" rel="stylesheet">
<style>
  :root {
    --stage: #b4b4b4;
    --cover: #050505;
    --ink: #ffffff;
    --panel-top: #d9d9db;
    --panel-mid: #1b1b1b;
    --portrait-frame: #19c6d6;
    --photo-light: #5c5c5c;
    --photo-mid: #333333;
    --photo-dark: #0b0b0b;
  }
  * { margin: 0; padding: 0; box-sizing: border-box; }
  html, body { width: 1200px; height: 1200px; overflow: hidden; }
  body {
    background: var(--stage);
    position: relative;
    font-family: "Tinos", "Times New Roman", serif;
    color: var(--ink);
  }

  .cover { position: absolute; top: 280px; width: 432px; height: 618px; background: var(--cover); }
  .cover--back { left: 162px; }
  .cover--front { left: 625px; }

  /* Back cover */
  .back-panel {
    position: absolute; left: 32px; top: 30px; width: 368px; height: 557px;
    background: linear-gradient(180deg, var(--panel-top) 0%, #8a8a8c 18%, var(--panel-mid) 40%, #000 62%);
  }
  .author-portrait {
    position: absolute; left: 30px; top: 30px; width: 103px; height: 112px;
    border: 2px solid var(--portrait-frame);
    background:
      radial-gradient(ellipse 45% 40% at 50% 40%, #4a4a4a 0%, transparent 100%),
      radial-gradient(ellipse at 50% 55%, #2a2a2a 0%, #0e0e0e 70%, #050505 100%);
  }
  .author-caption {
    position: absolute; left: 30px; top: 148px; width: 103px; text-align: center;
    font-size: 11.5px; font-weight: 700;
  }
  .excerpt {
    position: absolute; left: 30px; top: 212px; width: 308px;
    font-size: 11.6px; font-weight: 700; line-height: 18px;
  }
  .excerpt p { margin-bottom: 18px; }
  .excerpt-sign {
    position: absolute; right: 37px; top: 518px;
    font-size: 11.6px; font-weight: 700;
  }

  /* Front cover */
  .front-photo {
    position: absolute; left: 25px; top: 44px; width: 370px; height: 550px;
    background:
      radial-gradient(ellipse 22% 14% at 50% 24%, var(--photo-light) 0%, transparent 100%),
      radial-gradient(ellipse 38% 45% at 50% 58%, #2b2b2b 0%, transparent 100%),
      radial-gradient(ellipse 70% 60% at 50% 35%, var(--photo-mid) 0%, #1a1a1a 55%, var(--photo-dark) 100%);
  }
  .title {
    position: absolute; right: 61px; top: 40px; text-align: right;
    font-family: "Arimo", Arial, sans-serif; font-weight: 700; line-height: 1;
  }
  .title-main { display: block; font-size: 42px; letter-spacing: 0.3px; }
  .title-sub { display: block; font-size: 20px; margin-top: 5px; }
  .front-credits {
    position: absolute; right: 61px; top: 498px; text-align: right; font-weight: 700;
  }
  .series { display: block; font-size: 21px; line-height: 24px; }
  .subtitle { display: block; font-size: 14px; line-height: 22px; margin-top: 1px; }
  .byline { display: block; font-size: 11.6px; line-height: 14px; }
</style>
</head>
<body>
  <section class="cover cover--back">
    <div class="back-panel">
      <div class="author-portrait" role="img" aria-label="Author portrait photograph"></div>
      <div class="author-caption">Lorcan Vittel</div>
      <div class="excerpt">
        <p>Excerpt from Chapter One like this :</p>
        <p>As years have gone by I have become much more conscious about my problem with stuttering, more able to relax my muscles to alleviate it. At the age of 20, I realized that stuttering is like a demon in my head that needs to be killed and that nothing is wrong with me. Furthermore, no one can help me but myself. I’m holding the key of my future. Everything is just in my head.</p>
        <p>With this book, I want to help you realize that nobody can help you fix your stuttering better than yourself. There’s no quick-get-rid-of-stuttering cure. The cure lies inside of you.</p>
      </div>
      <div class="excerpt-sign">- Lorcan Vittel, excerpt from Chapter One</div>
    </div>
  </section>

  <section class="cover cover--front">
    <div class="front-photo" role="img" aria-label="Author standing in a dark shirt against a black backdrop"></div>
    <h1 class="title">
      <span class="title-main">Lanterns Past</span>
      <span class="title-sub">Harbour</span>
    </h1>
    <div class="front-credits">
      <span class="series">Tide Notes</span>
      <span class="subtitle">7 paths to gardening calmly always</span>
      <span class="byline">- Lorcan Vittel</span>
    </div>
  </section>
</body>
</html>
```